CalmHarbor Homepage and Landing Pages

Please see detailed brief.

CalmHarbor is Australia’s newest online therapy and mental health service. We allow patients from across australia to connect with Mental health practitioners from across Australia. Our mission is to remove the friction in gaining support for mental health related issues.

Number of Pages Required

1 page

Font styles to use
Sans Serif

Colors
33a6d7
0293ce
3277b5
0255a3
acd136
9bcb3c

Requirements
Must have
• Please see detailed brief.
Nice to have
• Please see detailed brief
Should not have

```html
<!DOCTYPE html>
<html lang="en">
<head>
<meta charset="utf-8">
<title>CalmHarbor – Online Therapy</title>
<link href="https://fonts.googleapis.com/css2?family=Poppins:wght@300;400;500;600;700&display=swap" rel="stylesheet">
<style>
:root{
  --blue:#1e9af5;
  --blue-mid:#1a7fe0;
  --blue-deep:#0a4fc0;
  --navy:#0b3f9e;
  --green:#9bcb3c;
  --ink:#1a1a1a;
  --muted:#666;
  --paper:#ffffff;
  --soft:#f5f6f7;
  --footer:#0d0d0d;
}
*{box-sizing:border-box;margin:0;padding:0}
html,body{width:1200px;height:4276px;overflow:hidden}
body{font-family:"Poppins",sans-serif;color:var(--ink);background:var(--paper);position:relative}
.abs{position:absolute}

/* header */
.site-header{position:absolute;left:0;top:0;width:1200px;height:72px;background:var(--paper);display:flex;align-items:center;z-index:2}
.brand{display:flex;align-items:center;gap:10px;margin-left:24px;font-weight:600;font-size:26px;color:var(--blue)}
.brand-dot{width:16px;height:16px;border-radius:50%;background:var(--blue)}
.main-nav{display:flex;gap:46px;margin-left:120px;font-size:14px;color:#333}
.main-nav .active{color:var(--blue);position:relative}
.main-nav .active::after{content:"";position:absolute;left:50%;top:-14px;width:6px;height:6px;margin-left:-3px;border-radius:50%;background:var(--blue)}
.sign-in{margin-left:auto;width:240px;height:72px;background:var(--blue);color:#fff;font-size:16px;display:flex;align-items:center;justify-content:center}

/* hero */
.hero{position:absolute;left:0;top:72px;width:1200px;height:548px;background:linear-gradient(100deg,#2b2f33 0%,#3d4247 45%,#5a5f63 100%)}
.hero h1{position:absolute;left:172px;top:130px;font-weight:500;font-size:42px;line-height:52px;color:#fff}
.hero p{position:absolute;left:172px;top:240px;font-size:20px;color:#fff}
.hero .btn{position:absolute;top:300px;height:66px;width:236px;display:flex;align-items:center;justify-content:center;color:#fff;font-size:16px}
.btn-book{left:172px;background:var(--blue)}
.btn-find{left:408px;background:var(--green)}

/* about */
.about-panel{position:absolute;left:0;top:620px;width:600px;height:532px;background:var(--blue);color:#fff;padding:78px 0 0 176px}
.about-panel h2{font-size:50px;line-height:58px;font-weight:600}
.about-panel p{margin-top:22px;width:360px;font-size:13px;line-height:22px;opacity:.92}
.btn-dark{display:inline-flex;align-items:center;justify-content:center;margin-top:30px;width:130px;height:46px;background:var(--navy);color:#fff;font-size:14px}
.about-photo{position:absolute;left:600px;top:620px;width:600px;height:532px;background:linear-gradient(135deg,#e8e2d8,#c9b9a3 55%,#8a7a66)}

/* services */
.services{position:absolute;left:0;top:1152px;width:1200px;height:1120px;background:var(--soft)}
.section-title{position:absolute;width:1200px;text-align:center;font-weight:600;font-size:46px;color:var(--ink)}
.card{position:absolute;width:404px;height:460px;background:var(--paper);box-shadow:0 4px 18px rgba(0,0,0,.07)}
.card-photo{height:268px}
.card h3{margin:22px 0 0 34px;font-size:18px;font-weight:600}
.card p{margin:8px 34px 0;font-size:13px;line-height:20px;color:var(--muted)}
.btn-small{display:inline-flex;align-items:center;justify-content:center;margin:18px 0 0 34px;width:104px;height:34px;background:var(--blue-mid);color:#fff;font-size:12px}

/* appointment banner */
.appt{position:absolute;left:176px;top:2272px;width:844px;height:568px}
.appt-photo{position:absolute;left:0;top:0;width:844px;height:408px;background:linear-gradient(90deg,#3a3a3a 0%,#6f6a64 40%,#c9c4bc 70%,#e6e3de 100%)}
.appt h2{position:absolute;left:500px;top:128px;width:330px;font-size:34px;line-height:44px;font-weight:600;color:var(--ink)}
.tile{position:absolute;top:408px;height:160px;width:282px;display:flex;flex-direction:column;align-items:center;justify-content:center;text-align:center;color:#fff}
.tile h4{font-size:22px;font-weight:600}
.tile p{font-size:12px;line-height:18px;margin-top:6px;width:170px}
.tile-travel{left:0;background:var(--blue)}
.tile-clinic{left:282px;background:var(--blue-deep)}
.tile-find{left:564px;width:280px;background:var(--green);color:var(--ink)}

/* testimonials */
.quote-mark{position:absolute;left:582px;top:3040px;width:36px;height:36px;border-radius:50%;background:#222;color:#fff;font-size:26px;line-height:44px;text-align:center;font-weight:700}
.quote-text{position:absolute;left:300px;top:3100px;width:600px;text-align:center;font-size:14px;line-height:24px;color:var(--muted)}
.quote-name{position:absolute;left:0;top:3214px;width:1200px;text-align:center;font-size:14px;font-weight:600}
.arrow{position:absolute;top:3086px}

/* booking */
.booking{position:absolute;left:0;top:3340px;width:1200px;height:540px;background:var(--blue)}
.booking h2{position:absolute;left:176px;top:150px;font-size:48px;line-height:56px;font-weight:600;color:#fff}
.booking p{position:absolute;left:176px;top:290px;width:460px;font-size:13px;line-height:21px;color:#fff;opacity:.92}
.form{position:absolute;left:712px;top:90px;width:316px}
.field{height:40px;background:#fff;margin-bottom:14px;font-size:12px;color:#888;padding:0 12px;display:flex;align-items:center}
.field.date{justify-content:space-between}
.field.message{height:112px;align-items:flex-start;padding-top:10px}
.submit{height:40px;background:var(--navy);color:#fff;font-size:15px;display:flex;align-items:center;justify-content:center}

/* footer */
.site-footer{position:absolute;left:0;top:3880px;width:1200px;height:396px;background:var(--footer);color:#ddd}
.footer-brand{position:absolute;left:0;top:44px;width:1200px;display:flex;justify-content:center;align-items:center;gap:12px;font-size:42px;font-weight:500;color:#fff}
.footer-brand .brand-dot{width:22px;height:22px}
.col{position:absolute;top:148px;font-size:12px;line-height:26px;color:#bbb}
.col h5{font-size:15px;font-weight:600;color:#fff;margin-bottom:10px}
.contact-row{display:flex;align-items:center;gap:10px}
.social{position:absolute;top:340px;width:22px;height:22px;border-radius:50%;background:var(--blue)}
.copyright{position:absolute;left:176px;top:346px;font-size:12px;color:#aaa}
</style>
</head>
<body>

<header class="site-header">
  <div class="brand"><span class="brand-dot"></span>CalmHarbor</div>
  <nav class="main-nav">
    <span class="active">Home</span><span>Contact</span><span>Our Team</span><span>Practitioner Information</span><span>About Us</span>
  </nav>
  <div class="sign-in">Patient Sign In</div>
</header>

<section class="hero" role="img" aria-label="Person on a video call with a therapist on a laptop, dark overlay">
  <h1>Psychologists &amp; personal<br>Wellness professionals</h1>
  <p>Book your online appointment in minutes, 24/7</p>
  <span class="btn btn-book">Book an Appointment</span>
  <span class="btn btn-find">Find a Practitioner</span>
</section>

<section class="about-panel">
  <h2>What is<br>CalmHarbor?</h2>
  <p>CalmHarbor is Australia's newest online therapy and mental health service. We allow patients from across Australia to connect with mental health practitioners. Our mission is to remove the friction in gaining support for mental health related issues.</p>
  <span class="btn-dark">Read More</span>
</section>
<div class="about-photo" role="img" aria-label="Older woman at a desk on a video call with a practitioner"></div>

<section class="services">
  <h2 class="section-title" style="top:46px">Our Services</h2>

  <article class="card" style="left:176px;top:120px">
    <div class="card-photo" role="img" aria-label="Person holding a tablet during a video session" style="background:linear-gradient(135deg,#d9c8b2,#a8937a)"></div>
    <h3>Mental Health</h3>
    <p>Lorem ipsum dolor sit amet, consectetur adipiscing elit, sed do eiusmod tempor incidid</p>
    <span class="btn-small">Read More</span>
  </article>
  <article class="card" style="left:620px;top:120px">
    <div class="card-photo" role="img" aria-label="Woman with headphones talking on a video call" style="background:linear-gradient(135deg,#cfc9c0,#6b5a4c)"></div>
    <h3>Online therapy</h3>
    <p>Lorem ipsum dolor sit amet, consectetur adipiscing elit, sed do eiusmod tempor incidid</p>
    <span class="btn-small">Read More</span>
  </article>
  <article class="card" style="left:176px;top:608px">
    <div class="card-photo" role="img" aria-label="Stressed person holding their head" style="background:linear-gradient(135deg,#b9b4ae,#4d4a47)"></div>
    <h3>Finibus Bonorum</h3>
    <p>Lorem ipsum dolor sit amet, consectetur adipiscing elit, sed do eiusmod tempor incidid</p>
    <span class="btn-small">Read More</span>
  </article>
  <article class="card" style="left:620px;top:608px">
    <div class="card-photo" role="img" aria-label="Person sitting on the floor hugging their knees" style="background:linear-gradient(135deg,#8c8a86,#3c3b39)"></div>
    <h3>Finibus Bonorum</h3>
    <p>Lorem ipsum dolor sit amet, consectetur adipiscing elit, sed do eiusmod tempor incidid</p>
    <span class="btn-small">Read More</span>
  </article>
</section>

<section class="appt">
  <div class="appt-photo" role="img" aria-label="Woman at a laptop taking notes during an online consultation"></div>
  <h2>Book an appointment with our practitioners</h2>
  <div class="tile tile-travel"><h4>No Travel</h4><p>Lorem ipsum dolor sit amet, consectetur.</p></div>
  <div class="tile tile-clinic"><h4>No Clinics</h4><p>Lorem ipsum dolor sit amet, consectetur.</p></div>
  <div class="tile tile-find"><h4>Find a<br>Practitioner</h4></div>
</section>

<h2 class="section-title" style="top:2926px;font-size:44px">Our Happy Customers</h2>
<div class="quote-mark">“</div>
<p class="quote-text">Sed ut perspiciatis unde omnis iste natus error sit voluptatem accusantium doloremque laudantium, totam rem aperiam, eaque ipsa quae ab illo inventore veritatis et quasi architecto beatae vitae dicta sunt explicabo.</p>
<p class="quote-name">- Nora Ellison</p>
<svg class="arrow" style="left:176px" width="24" height="70" viewBox="0 0 24 70"><path d="M20 2 L4 35 L20 68" fill="none" stroke="#bbb" stroke-width="2"/></svg>
<svg class="arrow" style="left:1000px" width="24" height="70" viewBox="0 0 24 70"><path d="M4 2 L20 35 L4 68" fill="none" stroke="#bbb" stroke-width="2"/></svg>

<section class="booking">
  <h2>Book your<br>online appointment</h2>
  <p>Sed ut perspiciatis unde omnis iste natus error sit voluptatem accusantium doloremque laudantium, totam rem aperiam eaque ipsa quae ab illo inventore veritatis et quasi.</p>
  <div class="form">
    <div class="field">Name</div>
    <div class="field">Email</div>
    <div class="field">Phone</div>
    <div class="field date">Date
      <svg width="10" height="6" viewBox="0 0 10 6"><path d="M0 0 L5 6 L10 0Z" fill="#888"/></svg>
    </div>
    <div class="field message">Message</div>
    <div class="submit">Submit</div>
  </div>
</section>

<footer class="site-footer">
  <div class="footer-brand"><span class="brand-dot"></span>CalmHarbor</div>

  <div class="col" style="left:176px">
    <h5>Contact</h5>
    <div class="contact-row">
      <svg width="12" height="16" viewBox="0 0 12 16"><path d="M6 0a6 6 0 0 0-6 6c0 4.5 6 10 6 10s6-5.5 6-10a6 6 0 0 0-6-6zm0 8.5A2.5 2.5 0 1 1 6 3.5a2.5 2.5 0 0 1 0 5z" fill="#bbb"/></svg>
      <span>12 Harbour Lane, Sampleton 2000</span>
    </div>
    <div class="contact-row">
      <svg width="14" height="14" viewBox="0 0 14 14"><path d="M3 1l2 3-1.5 1.5a8 8 0 0 0 5 5L10 9l3 2-1 2.5C6 14 0 8 .5 2z" fill="#bbb"/></svg>
      <span>+00 1234 5678</span>
    </div>
    <div class="contact-row">
      <svg width="14" height="10" viewBox="0 0 14 10"><rect x=".5" y=".5" width="13" height="9" fill="none" stroke="#bbb"/><path d="M.5 .5 L7 6 L13.5 .5" fill="none" stroke="#bbb"/></svg>
      <span>hello@calmharbor.example</span>
    </div>
  </div>

  <div class="col" style="left:444px">
    <h5>Services</h5>
    <div>Lorem ipsum dolor</div><div>Consectetur adipiscing</div><div>Sed do eiusmod</div><div>Tempor incididunt</div>
  </div>

  <div class="col" style="left:688px">
    <h5>Links</h5>
    <div>Lorem ipsum dolor</div><div>Consectetur adipisc</div><div>Tempor magna aliqua</div><div>Minim veniam</div>
  </div>

  <div class="col" style="left:888px">
    <h5>Hours</h5>
    <div>Mon – Fri 8am – 8pm</div><div>Saturday 9am – 5pm</div><div>Sunday 10am – 4pm</div>
  </div>

  <span class="social" style="left:972px"></span>
  <span class="social" style="left:1002px"></span>
  <p class="copyright">Copyright 2020 All Rights Reserved</p>
</footer>

</body>
</html>
```